Poster design for "A Frame" Sign

I need a design for an A Frame sign. Measurements and Specifications here:
http://www.brodexsupply.com.au/pg/a-boards/ABPBBLKPRT-Print-Specs.pdf

Actually, it will need to be two designs, one with an arrow pointing left and one with an arrow pointing right, otherwise exactly the same.

LOGO to be used is attached. Colours of design should match logo and should also include orange tones.

The A Frame sign is to be put on the driveway of my home studio at a main road in a residential suburban area. Cars drive by at around 50 km/h, so there needs to be an eye catcher that there is a nurturing home massage studio here.

Logo can be left or right, somehow incorporated into the text below:
-
[Big header, ideally "LeHavre" font]
Tarova Calm
Massage Studio

[slightly smaller font, serif, with bullet points]
- Relaxation Massage
- Remedial Massage
- Pregnancy Massage
- Kahuna Massage

[big Arrow to the left/right - one for each side of the frame]

[sans serif font, same size as above]
Bookings essential!
ph 0491 857 604
www.tarovacalm.com.au

[serif font, same as above]
EFTPOS and instant health fund claims available.
-

Residential

f37022

```html
<!DOCTYPE html>
<html lang="en">
<head>
<meta charset="utf-8">
<title>Tarova Calm Massage Studio – A Frame Sign</title>
<link rel="stylesheet" href="https://fonts.googleapis.com/css2?family=Open+Sans:wght@600;700;800&display=swap">
<style>
  :root {
    --paper: #ffffff;
    --beige: #c6b89f;
    --beige-deep: #b9aa8f;
    --cream: #e2dbcb;
    --cream-light: #efeadf;
    --maroon: #7e1537;
    --magenta: #e9478f;
    --leaf: #5daa3a;
    --leaf-dark: #2f6e22;
    --ink: #231f20;
    --white: #ffffff;
  }
  * { margin: 0; padding: 0; box-sizing: border-box; }
  html, body {
    width: 896px; height: 1200px; overflow: hidden;
    background: var(--paper);
    font-family: "Open Sans", Arial, sans-serif;
  }
  .sign {
    position: absolute; left: 84px; top: 40px;
    width: 734px; height: 1086px;
    background: var(--beige);
    overflow: hidden;
  }
  .backdrop { position: absolute; inset: 0; width: 734px; height: 1086px; }
  .title {
    position: absolute; left: 61px; top: 16px; width: 290px;
    text-align: center; color: var(--ink);
    font-weight: 700; font-size: 58px; line-height: 74px;
  }
  .brand-mark {
    position: absolute; left: 367px; top: 76px;
    width: 256px; height: 256px; border-radius: 50%;
    background: var(--magenta);
    border: 16px solid var(--maroon);
    display: flex; align-items: center; justify-content: center;
    color: var(--white); font-weight: 700; font-size: 38px;
    text-align: center; line-height: 1.1;
  }
  .offer-band {
    position: absolute; left: 0; top: 348px; width: 734px; height: 82px;
    background: var(--maroon); color: var(--white);
    display: flex; align-items: center; justify-content: center;
    font-weight: 700; font-size: 40px; letter-spacing: -0.3px;
  }
  .services {
    position: absolute; left: 0; top: 449px; width: 734px; list-style: none;
  }
  .services li {
    display: flex; align-items: center; height: 54px;
    font-weight: 700; font-size: 41px; color: var(--ink);
    letter-spacing: -0.3px;
  }
  .services .bullet { width: 72px; height: 22px; margin-left: 89px; margin-right: 49px; flex: none; }
  .direction-arrow { position: absolute; left: 0; top: 700px; width: 734px; height: 160px; }
  .booking-band {
    position: absolute; left: 0; top: 882px; width: 734px; height: 204px;
    background: var(--maroon); color: var(--white);
    text-align: center; font-weight: 700;
  }
  .booking-band .line { font-size: 43px; line-height: 53px; }
  .booking-band .first { padding-top: 2px; }
  .booking-band .payments { font-size: 22px; line-height: 40px; }
</style>
</head>
<body>
  <main class="sign">
    <svg class="backdrop" viewBox="0 0 734 1086" aria-hidden="true">
      <path d="M560 0 H734 V1086 H0 V640 C220 700 420 560 470 350 C500 220 530 90 560 0 Z" fill="var(--cream)"/>
      <path d="M640 0 H734 V140 C700 100 670 50 640 0 Z" fill="var(--cream-light)"/>
      <path d="M0 600 C180 690 330 760 520 882 H0 Z" fill="var(--beige-deep)" opacity="0.55"/>
    </svg>
    <svg class="backdrop" viewBox="0 0 734 1086" role="img" aria-label="Soft leaf and vine decoration">
      <defs>
        <radialGradient id="foliage" cx="50%" cy="50%" r="50%">
          <stop offset="0" stop-color="#b7c59a" stop-opacity="0.45"/>
          <stop offset="1" stop-color="#b7c59a" stop-opacity="0"/>
        </radialGradient>
      </defs>
      <ellipse cx="110" cy="70" rx="150" ry="110" fill="url(#foliage)"/>
      <ellipse cx="650" cy="840" rx="150" ry="110" fill="url(#foliage)"/>
      <ellipse cx="620" cy="560" rx="120" ry="90" fill="url(#foliage)"/>
    </svg>

    <h1 class="title">Tarova<br>Calm<br>Massage<br>Studio</h1>

    <div class="brand-mark">Tarova<br>Calm</div>

    <div class="offer-band">NOW OFFERING Lumera Massage</div>

    <ul class="services">
      <li><svg class="bullet" viewBox="0 0 72 22" aria-hidden="true"><path d="M2 11 C20 -2 52 -2 70 11 C52 24 20 24 2 11 Z" fill="var(--leaf)" stroke="var(--leaf-dark)" stroke-width="1.5"/><path d="M6 11 H66" stroke="var(--leaf-dark)" stroke-width="1.2"/></svg>Relaxation Massage</li>
      <li><svg class="bullet" viewBox="0 0 72 22" aria-hidden="true"><path d="M2 11 C20 -2 52 -2 70 11 C52 24 20 24 2 11 Z" fill="var(--leaf)" stroke="var(--leaf-dark)" stroke-width="1.5"/><path d="M6 11 H66" stroke="var(--leaf-dark)" stroke-width="1.2"/></svg>Remedial Massage</li>
      <li><svg class="bullet" viewBox="0 0 72 22" aria-hidden="true"><path d="M2 11 C20 -2 52 -2 70 11 C52 24 20 24 2 11 Z" fill="var(--leaf)" stroke="var(--leaf-dark)" stroke-width="1.5"/><path d="M6 11 H66" stroke="var(--leaf-dark)" stroke-width="1.2"/></svg>Pregnancy Massage</li>
      <li><svg class="bullet" viewBox="0 0 72 22" aria-hidden="true"><path d="M2 11 C20 -2 52 -2 70 11 C52 24 20 24 2 11 Z" fill="var(--leaf)" stroke="var(--leaf-dark)" stroke-width="1.5"/><path d="M6 11 H66" stroke="var(--leaf-dark)" stroke-width="1.2"/></svg>Kahuna Massage</li>
    </ul>

    <svg class="direction-arrow" viewBox="0 0 734 160" role="img" aria-label="Arrow pointing right">
      <path d="M93 62 H540 V14 L680 80 L540 146 V98 H93 Z" fill="var(--magenta)"/>
    </svg>

    <section class="booking-band">
      <p class="line first">Bookings essential!</p>
      <p class="line">ph 0491 857 604</p>
      <p class="line">www.tarovacalm.com.au</p>
      <p class="payments">EFTPOS and instant health fund claims available.</p>
    </section>
  </main>
</body>
</html>
```